Catalogue for Eco friendly products

HI We have 2 brands - logos attached
Lumatotesnz
Brimwrap

We would like a catalog of these products :

Size of the catalogue: A4 Size

Lumatotes - ( www.lumatotes.co.nz)
Cotton bags
Canvas bags
Jute bags
Non woven bags
Tindlewag poop bags

Brimwrap
Degradable bin liners
Compostable bin liners
Recycled bin liners
Paper bags
Customised packaging

All products need to be on A4 page which can be inserted in a folder, the main reason for that to make sales presentation as per the customer requirement. All customers don't need all the products.

We are looking for the designer to make a clean feel where both the logos sit comfortably with each other.

We will need 2 main designs:
1 will be the outside folder design
Inside Catalog for the products with place holders for the photographs and words which can be limited to 10-20 words to ensure that design looks uniform. All products are on our website to provide you with an idea of what we are looking for.

Brimwrap packaging logo is included for your reference to get a feel of the products.
Any other information please let me know.
Thanks

Target Market(s)

B2B- Businesses , purchase manager , event managers, Organic shop owners

Font styles to use
Serif
Sans Serif

Colors
add136
abd037
acd037
cadf82
9bcb3c
f37122

Requirements
Must have
• A Clean design and yet interesting , use of green colour is preferred for the design but complimentary earthy colors are ok
• TEXT in design: Attached for 1 product category : Cotton
Nice to have
• Please see the design inspirations which I like. Please note that these are just to give you an idea of what kind of design we would prefer and is to be used as our guidance to you.

```html
<!DOCTYPE html>
<html lang="en">
<head>
<meta charset="utf-8">
<title>Calico Cotton – Lumatotes Catalogue</title>
<link href="https://fonts.googleapis.com/css2?family=Open+Sans:wght@300;400;700&display=swap" rel="stylesheet">
<style>
  :root {
    --leaf: #8aa343;
    --stone: #8c8c8c;
    --ink: #222222;
    --paper: #ffffff;
    --backdrop: #ecebe6;
    --calico-light: #f3efe4;
    --calico-dark: #ddd6c4;
  }
  * { margin: 0; padding: 0; box-sizing: border-box; }
  html, body {
    width: 1200px; height: 1200px; overflow: hidden;
    background: var(--backdrop);
    font-family: "Open Sans", sans-serif;
  }
  .sheet-frame {
    position: absolute; left: 197px; top: 30px;
    width: 806px; height: 1140px; overflow: hidden;
  }
  .sheet {
    position: absolute; left: 0; top: 0;
    width: 868px; height: 1227px;
    background: var(--paper);
    transform: scale(0.9286); transform-origin: 0 0;
  }
  .masthead { position: absolute; left: 0; top: 0; width: 868px; height: 100px; }
  .category-label {
    position: absolute; left: 49px; top: 27px; width: 264px; height: 45px;
    border: 2px solid var(--paper);
    color: var(--paper); font-weight: 300; font-size: 23px;
    display: flex; align-items: center; justify-content: center;
  }
  .product-bar { position: absolute; left: 49px; width: 769px; height: 37px; }
  .product-bar svg { position: absolute; left: 0; top: 0; }
  .product-title {
    position: absolute; left: 30px; top: 0; line-height: 37px;
    color: var(--paper); font-weight: 700; font-size: 23px;
  }
  .product-size {
    position: absolute; right: 22px; top: 0; line-height: 35px;
    color: var(--paper); font-weight: 300; font-size: 15px; letter-spacing: -0.4px;
  }
  .product-photo {
    position: absolute;
    background: linear-gradient(160deg, var(--calico-light), var(--calico-dark));
  }
  .product-copy {
    position: absolute; left: 279px; width: 545px;
    color: var(--ink); font-size: 16.6px; line-height: 19.4px;
  }
  .product-copy h3 { font-size: 16.6px; font-weight: 700; }
  .cert-badge {
    position: absolute; left: 280px; top: 398px; width: 74px; height: 43px;
    background: #111111;
  }
  .contact-strip {
    position: absolute; left: 0; top: 1178px; width: 868px; height: 49px;
    background: var(--stone); color: var(--paper);
    font-size: 17px; display: flex; align-items: center; justify-content: center;
  }
  .contact-strip b { font-weight: 700; }
  .contact-strip .divider { margin: 0 8px; }
</style>
</head>
<body>
<div class="sheet-frame">
  <div class="sheet">

    <header class="masthead">
      <svg width="868" height="100" viewBox="0 0 868 100">
        <polygon points="0,0 758,0 790,100 0,100" fill="var(--leaf)"/>
        <polygon points="754,0 784,0 818,100 788,100" fill="var(--stone)"/>
      </svg>
      <div class="category-label">CALICO COTTON</div>
    </header>

    <!-- Fair trade bag -->
    <div class="product-bar" style="top:149px">
      <svg width="769" height="37" viewBox="0 0 769 37">
        <rect width="769" height="37" fill="var(--stone)"/>
        <polygon points="0,0 502,0 492,37 0,37" fill="var(--leaf)"/>
      </svg>
      <div class="product-title">FAIRSHARE BAG</div>
      <div class="product-size">36.5cm(w) X 39cm(h) X 8.5cm(g)</div>
    </div>
    <div class="product-photo" style="left:84px;top:199px;width:140px;height:260px" role="img" aria-label="Photo of a natural calico tote bag with long handles and a printed slogan"></div>
    <div class="product-copy" style="top:205px">
      <h3>What is Fairshare?</h3>
      <p>Fairshare is about better prices, decent working conditions, local sustainability, and fair terms of trade for farmers and workers in the developing world. By requiring companies to pay sustainable prices (which must never fall lower than the market price), Fairshare addresses the injustices of conventional trade, which traditionally discriminates against the poorest, weakest producers. It enables them to improve their position and have more control over their lives.</p>
    </div>
    <div class="cert-badge" role="img" aria-label="Certification badge"></div>

    <!-- EC-04 -->
    <div class="product-bar" style="top:475px">
      <svg width="769" height="37" viewBox="0 0 769 37">
        <rect width="769" height="37" fill="var(--stone)"/>
        <polygon points="0,0 502,0 492,37 0,37" fill="var(--leaf)"/>
      </svg>
      <div class="product-title">EC-04 TOTE WITH GUSSET BAG</div>
      <div class="product-size">38cm(w) X 36cm(h) X 9.5cm(g)</div>
    </div>
    <div class="product-photo" style="left:67px;top:524px;width:167px;height:255px" role="img" aria-label="Photo of a calico tote bag with gusset and a printed client logo"></div>
    <div class="product-copy" style="top:532px">
      <p>This tote with gusset is the second most available bag in our calico range. Next to our promotional this one provides additional space, making this bag suitable for shopping, for a quick run to the gym or for toting the togs and towel to the beach, getting your logo seen in the most interesting places.</p>
    </div>

    <!-- EC-05 -->
    <div class="product-bar" style="top:802px">
      <svg width="769" height="37" viewBox="0 0 769 37">
        <rect width="769" height="37" fill="var(--stone)"/>
        <polygon points="0,0 502,0 492,37 0,37" fill="var(--leaf)"/>
      </svg>
      <div class="product-title">EC-05 PROMOTIONAL BAG</div>
      <div class="product-size" style="right:64px">37cm(w) X 41cm(h)</div>
    </div>
    <div class="product-photo" style="left:66px;top:849px;width:163px;height:260px" role="img" aria-label="Photo of a calico promotional bag with bold printed yoga slogan"></div>
    <div class="product-copy" style="top:858px">
      <p>This is our star! Our promotional bag comes in its natural state or in black is our most economical bag option for fundraising, promotional giveaways, birthday parties, or those things not requiring too much space! With an imagination, the sky’s the limit for these beauties. (Lumatotes Tip: For rainy days get the kids to decorate their own bag.)</p>
    </div>

    <footer class="contact-strip">
      Email&nbsp;<b>bags@lumatotes.co.nz</b><span class="divider">|</span>Phone&nbsp;<b>+64 9 555-0142</b><span class="divider">|</span>Fax&nbsp;<b>+64 9 555-0187</b>
    </footer>
  </div>
</div>
</body>
</html>
```